Byte Wardens Inc. IT Services and Sales

We need a new business card design for our new company. We have a current logo but are open and encourage any redesigns.

Byte Wardens is derived in our history from computer gaming. (Nebulith References, STORM UNBROKEN!!!). We as a group have been together since high school (2002). Our friendships brought us together and now we are all business partners providing IT Support and Consultation Services ranging from fixing small issues like printers, home networking, pc building to custom application development and managed cloud and it networks for our clients.
We would like our design to communicate that we strive to be the best (we are born gamers and have a highly competitive instinct) and offer solutions to problems that other companies just simply say we can't do it. We are always looking to go above and beyond for our clients, learning our clients business and figuring out ways to help them make more money by optimizing the way they do business, offering solutions so they can grow their business and helping everyone utilize the technology they have or advise them with the technology they need to succeed.

Attached are things we have on our computers and logo's we have used.
One is a desktop background
while the other should be our logo.

Again, we are open to and encourage any logo redesigns in hope things can help with the direction we are looking into.

Please add a place for email as our current cards have no email and it makes us very sad.
Updates

Hi All,

Just wanted to say thank you for all those who submitted a design. We've updated our project to include the fact that we are open and encourage a logo redesign. Also, this project is now committed to payment.

Target Market(s)

We will be handing these out to all our future business prospects. Prospects are usually business owners that can be in any industry. They look to us to be cutting edge or professional.

Industry/Entity Type

High School

Requirements
Must have
• name, title, work, fax, and cell phone, address and email

```html
<!DOCTYPE html>
<html lang="en">
<head>
<meta charset="utf-8">
<title>Byte Wardens – Business Card</title>
<link rel="stylesheet" href="https://fonts.googleapis.com/css2?family=Electrolize&display=swap">
<style>
  :root {
    --bg: #e6e3df;
    --card: #0c0c0c;
    --accent: #e0552b;
    --white: #ffffff;
    --text: #f2f2f2;
    --panel-light: #3a3a3a;
    --panel-dark: #0a0a0a;
  }
  * { margin: 0; padding: 0; box-sizing: border-box; }
  html, body {
    width: 1200px; height: 937px; overflow: hidden;
    background: var(--bg);
    font-family: "Electrolize", "Trebuchet MS", sans-serif;
  }
  .card {
    position: absolute; left: 100px; top: 182px;
    width: 1000px; height: 572px;
    background: var(--card);
    overflow: hidden;
    box-shadow: 0 18px 40px rgba(0,0,0,.25);
  }
  .edge-bands { position: absolute; left: 0; top: 0; }
  .brand-panel {
    position: absolute; left: 585px; top: 0;
    width: 330px; height: 175px;
    background: radial-gradient(ellipse at 55% 45%, var(--panel-light) 0%, #1d1d1d 45%, var(--panel-dark) 100%);
    display: flex; align-items: center; justify-content: center; gap: 12px;
  }
  .brand-dot { width: 26px; height: 26px; border-radius: 50%; background: var(--accent); }
  .brand-name { color: var(--white); font-size: 34px; letter-spacing: 1px; }
  .person { position: absolute; left: 140px; top: 188px; }
  .person-name { color: var(--accent); font-size: 36px; letter-spacing: 2px; line-height: 1; }
  .person-title { color: var(--text); font-size: 23px; margin-top: 14px; margin-left: 6px; }
  .contacts { position: absolute; list-style: none; }
  .contacts-left { left: 150px; top: 300px; }
  .contacts-right { left: 565px; top: 222px; }
  .contact {
    display: flex; align-items: center; gap: 26px;
    height: 40px; margin-bottom: 18px;
    color: var(--text); font-size: 22px; letter-spacing: .5px; white-space: nowrap;
  }
  .label { color: var(--accent); margin-right: 8px; }
  .icon {
    width: 38px; height: 38px; background: var(--accent);
    display: flex; align-items: center; justify-content: center; flex: none;
  }
  .icon svg { width: 22px; height: 22px; }
</style>
</head>
<body>
  <div class="card">
    <svg class="edge-bands" width="120" height="572" viewBox="0 0 120 572">
      <polygon points="0,0 70,0 70,150 0,228" fill="var(--accent)"/>
      <polygon points="0,275 84,196 102,572 0,572" fill="var(--white)"/>
    </svg>

    <div class="brand-panel">
      <span class="brand-dot"></span>
      <span class="brand-name">Byte Wardens</span>
    </div>

    <div class="person">
      <div class="person-name">MARCUS VALE</div>
      <div class="person-title">Managing Director</div>
    </div>

    <ul class="contacts contacts-left">
      <li class="contact">
        <span class="icon"><svg viewBox="0 0 24 24"><path d="M12 2a7 7 0 0 0-7 7c0 5 7 13 7 13s7-8 7-13a7 7 0 0 0-7-7zm0 9.5A2.5 2.5 0 1 1 12 6.5a2.5 2.5 0 0 1 0 5z" fill="var(--white)"/></svg></span>
        48 Relay Street, Dunmore
      </li>
      <li class="contact">
        <span class="icon"><svg viewBox="0 0 24 24"><path d="M6.6 10.8a15 15 0 0 0 6.6 6.6l2.2-2.2a1 1 0 0 1 1-.25 11.4 11.4 0 0 0 3.6.57 1 1 0 0 1 1 1V20a1 1 0 0 1-1 1A17 17 0 0 1 3 4a1 1 0 0 1 1-1h3.5a1 1 0 0 1 1 1c0 1.25.2 2.45.57 3.6a1 1 0 0 1-.25 1z" fill="var(--white)"/></svg></span>
        <span><span class="label">Work</span>555 014 2207</span>
      </li>
      <li class="contact">
        <span class="icon"><svg viewBox="0 0 24 24"><rect x="3" y="6" width="18" height="12" fill="var(--white)"/><path d="M3 6l9 7 9-7" fill="none" stroke="var(--accent)" stroke-width="1.6"/></svg></span>
        marcus@bytewardens.net
      </li>
    </ul>

    <ul class="contacts contacts-right">
      <li class="contact">
        <span class="icon"><svg viewBox="0 0 24 24" fill="none" stroke="var(--white)" stroke-width="1.6"><circle cx="12" cy="12" r="9"/><ellipse cx="12" cy="12" rx="4" ry="9"/><line x1="3" y1="12" x2="21" y2="12"/><line x1="5" y1="7.5" x2="19" y2="7.5"/><line x1="5" y1="16.5" x2="19" y2="16.5"/></svg></span>
        www.bytewardens.net
      </li>
      <li class="contact">
        <span class="icon"><svg viewBox="0 0 24 24"><rect x="7" y="2" width="10" height="20" rx="2" fill="var(--white)"/><rect x="9" y="5" width="6" height="11" fill="var(--accent)"/><circle cx="12" cy="19" r="1.2" fill="var(--accent)"/></svg></span>
        <span><span class="label">Cell</span>555 014 2290</span>
      </li>
      <li class="contact">
        <span class="icon"><svg viewBox="0 0 24 24"><rect x="7" y="3" width="10" height="6" fill="var(--white)"/><rect x="3" y="9" width="18" height="8" rx="1" fill="var(--white)"/><rect x="7" y="14" width="10" height="7" fill="var(--white)" stroke="var(--accent)" stroke-width="1.2"/></svg></span>
        <span><span class="label">Fax</span>555 014 2291</span>
      </li>
    </ul>
  </div>
</body>
</html>
```